Ortel Ridge Wine Club-The Velvet Roll

We are a new aspirational brand of fine Tasmania Wine. We need a commitment club poster which appeals to the ego.We have one opportunity to get customers to sign up and that is when they visit at the cellar door. This club is the core of our business.

The brand is a clean, pure , simple brand, black and white very sophiscated.
This is a top end product.

Our Commitment Club is named The Velvet Roll which is a play on words. Tradionally the velvet roll is a list of people that you dont want to do business with. So we are turning this on its had.

You need to make this poster sharp, desirable, possibly sexy but masculine. Im thinking Conrad Vale . It doesnt matter the client will be 40 up fashion consious looking for something new , exclusive , something there peers don't have.

I dont like busy! make it clean clear and basically undeniable. The client must not be able to resist the offer.

www.ortelridge-example.com.au

Target Market(s)

Appreciator 40-60 male wants to be recognised fashion consious sophiscated has money and wants to part of something exclusive.

A feeling that you are part of something that only a few are. Exclusive

Maybe an imagine of beautiful people 30/40ish I want to be drinking Ortel Wine / in the velvet roll

Industry/Entity Type

Fashion

Requirements
Must have
• Ortel Ridge Logo
ORTEL Bottles images

We produce only 1600 cases of wine each vintage. Therefore we have limited membership 001-999 for our club.
Award Winning Wines available exclusively from us.

Gold Member
We will reserve 2 cases of our limited vintage, to be delivered to you in May and Oct.
Single varietal or mixed cases. You receive a 15% discount.

Silver Member
We will reserve 1 case of our limited vintage to be delivered to you 6 bottles in May and 6 in Oct.
Single varietal or mixed cases. You receive a 10% discount.

To you exclusively from us not, available from any other retailers.

You will be invited to Velvet Roll Only Events and Tastings.
You will get preferential access to new and limited releases.
Members will be entered in a bi annual draw to win a 2 night stay here at the Ortel Weavers Lodge on the Freycinet Coast Tasmania.

Should not have
• VIP stamps,gimacs, anything that cheapens our brand.

We do not like busy posters please have white space

```html
<!DOCTYPE html>
<html lang="en">
<head>
<meta charset="utf-8">
<title>Ortel Ridge — The Velvet Roll</title>
<link rel="stylesheet" href="https://fonts.googleapis.com/css2?family=Arimo:wght@400&family=Cormorant+Garamond:ital,wght@0,500;1,600&family=Tinos:wght@400&display=swap">
<style>
  :root {
    --ink: #000000;
    --paper: #ffffff;
    --gold: #e3a43c;
    --bronze: #8a6a45;
    --bronze-dark: #3a2a1a;
    --panel: #1c1c1c;
    --haze: #2a2a2a;
    --bottle-deep: #2a0608;
    --bottle-mid: #6e1418;
  }
  * { margin: 0; padding: 0; box-sizing: border-box; }
  html, body {
    width: 848px; height: 1200px; overflow: hidden;
    background: var(--ink);
  }
  .poster {
    position: relative; width: 848px; height: 1200px; overflow: hidden;
    background:
      radial-gradient(ellipse 420px 520px at 330px 420px, var(--haze) 0%, rgba(0,0,0,0) 70%),
      radial-gradient(ellipse 360px 300px at 600px 120px, #181818 0%, rgba(0,0,0,0) 70%),
      var(--ink);
    color: var(--paper);
    font-family: "Arimo", Arial, sans-serif;
  }
  .brand-name {
    position: absolute; left: 0; width: 848px; top: 78px;
    text-align: center;
    font-family: "Cormorant Garamond", Georgia, serif;
    font-weight: 500; font-size: 92px; line-height: 1;
    color: var(--paper);
  }
  .club-title {
    position: absolute; left: 306px; top: 256px; width: 286px; height: 50px;
    background: linear-gradient(90deg, #0a0a0a, var(--panel) 50%, #0a0a0a);
    text-align: center;
    font-family: "Cormorant Garamond", Georgia, serif;
    font-style: italic; font-weight: 600; font-size: 38px; line-height: 50px;
    letter-spacing: 0.5px;
  }
  .bottle {
    position: absolute; left: 135px; top: 256px; width: 207px; height: 784px;
    border-radius: 60px 60px 10px 10px / 160px 160px 10px 10px;
    background: linear-gradient(90deg, var(--bottle-deep) 0%, var(--bottle-mid) 45%, var(--bottle-deep) 100%);
  }
  .right-column { position: absolute; left: 455px; width: 420px; text-align: center; }
  .section-tag {
    position: absolute; left: 492px; top: 338px; width: 178px; height: 36px;
    background: linear-gradient(90deg, var(--panel), #0a0a0a);
    font-family: "Cormorant Garamond", Georgia, serif;
    font-style: italic; font-weight: 600; font-size: 32px; line-height: 36px;
    text-align: center;
  }
  .benefits { top: 386px; font-size: 21px; line-height: 28px; }
  .benefit { padding: 0 10px; }
  .benefit-rule {
    height: 1px; margin: 8px 20px 10px 0;
    background: linear-gradient(90deg, rgba(227,164,60,0), var(--gold) 30%, var(--gold) 80%, rgba(227,164,60,0));
  }
  .tier-band {
    position: absolute; left: 413px; width: 385px; height: 40px;
    background: linear-gradient(90deg, var(--bronze-dark), var(--bronze) 50%, #1a120b);
    font-family: "Cormorant Garamond", Georgia, serif;
    font-style: italic; font-weight: 600; font-size: 34px; line-height: 40px;
    text-align: center;
  }
  .tier-band.gold { top: 624px; }
  .tier-band.silver { top: 839px; }
  .tier-copy { font-size: 21px; line-height: 30px; }
  .tier-copy.gold { top: 668px; }
  .tier-copy.silver { top: 884px; }
  .accent { color: var(--gold); }
  .discount { color: var(--gold); margin-top: 4px; }
  .draw-band {
    position: absolute; left: 0; top: 1076px; width: 848px; height: 82px;
    background: linear-gradient(90deg, #0c0805, var(--bronze) 50%, #0c0805);
    font-family: "Tinos", "Times New Roman", serif;
    font-size: 23px; line-height: 31px; text-align: center;
    padding-top: 10px;
  }
</style>
</head>
<body>
<main class="poster">
  <h1 class="brand-name">Ortel Ridge</h1>
  <h2 class="club-title">The Velvet Roll</h2>

  <div class="bottle" role="img" aria-label="Photograph of a bottle of Ortel Ridge 2011 Pinot Noir"></div>

  <h3 class="section-tag">Why Join?</h3>
  <div class="right-column benefits">
    <p class="benefit">- VIP access to Velvet Roll<br>Only tastings and events.</p>
    <div class="benefit-rule"></div>
    <p class="benefit">- Preferential access to first<br>releases and limited releases.</p>
    <div class="benefit-rule"></div>
    <p class="benefit">- Award winning wines<br>availible, exclusively from<br>Ortel Ridge.</p>
  </div>

  <h3 class="tier-band gold">Gold Membership</h3>
  <div class="right-column tier-copy gold">
    <p>Reserve <span class="accent">two</span>, single varietal<br>or mixed cases of our limited<br>vintage. Delivered to you in<br>May and October.</p>
    <p class="discount">15% Discount</p>
  </div>

  <h3 class="tier-band silver">Silver Membership</h3>
  <div class="right-column tier-copy silver">
    <p>Reserve <span class="accent">one</span>, single varietal<br>or mixed cases of our limited<br>vintage. Six bottles delivered<br>to you in May and October.</p>
    <p class="discount">10% Discount</p>
  </div>

  <p class="draw-band">Members will be entered into a bi annual draw to win a two night stay<br>here at the Ortel Weavers Lodge on the Freycinet Coast, Tasmania.</p>
</main>
</body>
</html>
```